Fast-casual chicken restaurant Brisket Barn needs a catering menu design

We need a catering menu designed for Brisket Barn. We are looking to design a 24x36in landscape menu board for our new catering menu. The catering memo attached includes our catering menu and Brisket Barn branding. More information about our brand can be found at https://brisketbarn-eats.example/.

```html
<!DOCTYPE html>
<html lang="en">
<head>
<meta charset="utf-8">
<title>Brisket Barn Catering Menu</title>
<link href="https://fonts.googleapis.com/css2?family=Montserrat:ital,wght@0,400;0,500;0,600;0,700;0,800;1,600&display=swap" rel="stylesheet">
<style>
:root{
  --wood:#8a5a34;
  --wood-dark:#5e3a1f;
  --yellow:#fdcd2e;
  --yellow-shade:#f0bd1d;
  --red:#d63a2a;
  --white:#ffffff;
  --navy:#34477a;
  --food-a:#c8561f;
  --food-b:#e9a23b;
  --plate:#1d1d1d;
}
*{box-sizing:border-box;margin:0;padding:0}
html,body{width:1200px;height:800px;overflow:hidden}
body{font-family:"Montserrat",sans-serif;background:linear-gradient(180deg,var(--wood) 0%,var(--wood-dark) 100%);position:relative}
.board{position:absolute;left:74px;top:124px;width:1054px;height:576px;background:var(--yellow)}
.photo{position:absolute;border-radius:40%}
.photo.platter{background:radial-gradient(circle at 50% 50%,var(--food-b) 0%,var(--food-a) 55%,#8c3015 100%)}
.photo.ribs{background:radial-gradient(circle at 50% 50%,#7a2a18 0%,#4a1a10 60%,var(--plate) 100%)}
.photo.rings{background:radial-gradient(circle,#e8b35a 0%,#c98a35 70%,transparent 100%)}
.photo.spread{border-radius:30% 30% 0 0;background:linear-gradient(90deg,#c8461c,#e79a3c 30%,#f1e3c9 50%,#e79a3c 70%,#c8461c)}
.abs{position:absolute}
.title{left:0;width:1200px;top:188px;text-align:center;font-weight:800;font-size:67px;letter-spacing:5px;color:var(--red);line-height:1}
.section{font-weight:800;font-size:21px;letter-spacing:3px;color:var(--white);line-height:1;white-space:nowrap}
.rule{height:3px;background:var(--white)}
.note{font-size:9px;font-style:italic;font-weight:600;color:var(--navy);letter-spacing:.3px}
.option{width:154px;height:192px;background:linear-gradient(90deg,var(--yellow-shade),var(--yellow) 30%);clip-path:polygon(0 0,100% 0,100% 100%,0 100%,0 19%,8px 15%,0 11%)}
.option .label{position:absolute;left:27px;top:22px;font-size:9px;letter-spacing:1.5px;color:var(--red);font-weight:500}
.option .name{position:absolute;left:27px;top:34px;font-size:23px;font-weight:800;color:var(--red);letter-spacing:.5px}
.option ul{position:absolute;left:27px;top:68px;list-style:none;font-size:12.5px;line-height:14px;color:var(--red);font-weight:500}
.option .price{position:absolute;left:27px;top:170px;font-size:11px;letter-spacing:2px;color:var(--red);font-weight:500;white-space:nowrap}
.pkg-name{font-size:20px;font-weight:800;color:var(--red);text-align:center;line-height:19px;width:130px}
.pkg{width:130px;height:157px;background:var(--red);border-radius:0 0 8px 8px;clip-path:polygon(0 0,42% 0,50% 10px,58% 0,100% 0,100% 100%,0 100%);color:var(--white);text-align:center;font-weight:500}
.pkg ul{list-style:none;font-size:12.5px;line-height:14px;position:absolute;left:0;width:100%}
.pkg .price{position:absolute;left:0;width:100%;bottom:20px;font-size:11.5px;letter-spacing:1.5px}
.item h3{font-size:18px;font-weight:800;color:var(--red);line-height:20px;letter-spacing:.2px}
.item p{font-size:10.5px;color:var(--red);font-weight:500;line-height:12px}
.item .muted{letter-spacing:1.5px}
.qty{display:grid;grid-template-columns:48px 48px;row-gap:8px;margin-top:3px}
.learn{font-size:13px;color:var(--navy);letter-spacing:1px;white-space:nowrap}
.learn strong{font-weight:800}
</style>
</head>
<body>
<div class="board"></div>

<div class="photo rings" style="left:-20px;top:80px;width:84px;height:170px" role="img" aria-label="Onion rings on the table"></div>
<div class="photo rings" style="left:1136px;top:80px;width:84px;height:170px" role="img" aria-label="Onion rings on the table"></div>
<div class="photo ribs" style="left:328px;top:-20px;width:136px;height:108px" role="img" aria-label="Plate of barbecue ribs"></div>
<div class="photo ribs" style="left:736px;top:-20px;width:136px;height:108px" role="img" aria-label="Plate of barbecue ribs"></div>
<div class="photo platter" style="left:-10px;top:-30px;width:330px;height:182px" role="img" aria-label="Platter of chicken wings"></div>
<div class="photo platter" style="left:880px;top:-30px;width:330px;height:182px" role="img" aria-label="Platter of chicken wings"></div>
<div class="photo platter" style="left:486px;top:-20px;width:226px;height:206px;border-radius:10px" role="img" aria-label="Tray of fried chicken tenders"></div>
<div class="photo ribs" style="left:-30px;top:600px;width:182px;height:136px" role="img" aria-label="Plate of barbecue ribs"></div>
<div class="photo ribs" style="left:1048px;top:600px;width:182px;height:136px" role="img" aria-label="Plate of barbecue ribs"></div>
<div class="photo spread" style="left:120px;top:680px;width:960px;height:140px" role="img" aria-label="Table spread of wings, tenders, waffle fries and dipping sauces"></div>

<h1 class="abs title">CATERING MENU</h1>

<h2 class="abs section" style="left:130px;top:270px">PER PERSON DEAL</h2>
<div class="abs rule" style="left:414px;top:279px;width:200px"></div>
<p class="abs note" style="left:130px;top:292px">&#9656; A MINIMUM OF 10 PEOPLE ARE NEEDED FOR THE PER PERSON DEALS</p>

<div class="abs option" style="left:150px;top:312px">
  <span class="label">OPTION 1</span><span class="name">SNACK</span>
  <ul><li>2 TENDERS</li><li>SAUCE</li><li>DRESSING</li><li>1 REG SIDE</li></ul>
  <span class="price">$7.00/PERSON</span>
</div>
<div class="abs option" style="left:309px;top:312px">
  <span class="label">OPTION 2</span><span class="name">PARTY</span>
  <ul><li>2 TENDERS</li><li>3 WINGS</li><li>SAUCE</li><li>DRESSING</li><li>1 REG SIDE</li><li>12OZ DRINK</li></ul>
  <span class="price">$11.00/PERSON</span>
</div>
<div class="abs option" style="left:465px;top:312px">
  <span class="label">OPTION 3</span><span class="name">FEAST</span>
  <ul><li>2 TENDERS</li><li>6 WINGS</li><li>SAUCE</li><li>DRESSING</li><li>1 REG SIDE</li><li>20OZ DRINK</li></ul>
  <span class="price">$15.00/PERSON</span>
</div>

<h2 class="abs section" style="left:670px;top:270px">PACKAGE DEALS</h2>
<div class="abs rule" style="left:916px;top:279px;width:166px"></div>

<div class="abs pkg-name" style="left:670px;top:315px">FAMILY</div>
<div class="abs pkg-name" style="left:812px;top:315px">TAILGATE</div>
<div class="abs pkg-name" style="left:953px;top:303px">HOUSE<br>PARTY</div>

<div class="abs pkg" style="left:670px;top:352px">
  <ul style="top:35px"><li>12 TENDERS</li><li>SAUCES</li><li>DRESSING</li><li>LARGE SIDE</li><li>2L</li></ul>
  <span class="price">$24.99</span>
</div>
<div class="abs pkg" style="left:812px;top:352px">
  <ul style="top:17px"><li>20 TENDERS</li><li>30 WINGS</li><li>SAUCES</li><li>2 PARTY SIDES</li><li>2 PARTY SALADS</li><li>DRESSINGS</li><li>2 2L</li></ul>
  <span class="price" style="bottom:22px">$75.99</span>
</div>
<div class="abs pkg" style="left:953px;top:352px">
  <ul style="top:17px"><li>20 TENDERS</li><li>60 WINGS</li><li>SAUCES</li><li>2 PARTY SIDES</li><li>2 PARTY SALADS</li><li>DRESSINGS</li><li>2 2L</li></ul>
  <span class="price">$155.99</span>
</div>

<h2 class="abs section" style="left:130px;top:523px">MAKE YOUR OWN DEAL</h2>
<div class="abs rule" style="left:478px;top:532px;width:604px"></div>

<div class="abs item" style="left:175px;top:555px">
  <h3>WINGS</h3>
  <div class="qty"><p>50<br><span class="muted">$7.00</span></p><p>75<br><span class="muted">$XX</span></p><p>100<br><span class="muted">$XX</span></p></div>
</div>
<div class="abs item" style="left:275px;top:555px">
  <h3>TENDERS</h3>
  <div class="qty"><p>30<br><span class="muted">$7.00</span></p><p>45<br><span class="muted">$XX</span></p><p>60<br><span class="muted">$XX</span></p></div>
</div>
<div class="abs item" style="left:401px;top:555px"><h3>WAFFLE<br>FRIES</h3><p>PARTY SIZE<br><span class="muted">$13.99</span></p></div>
<div class="abs item" style="left:537px;top:555px"><h3>GARLIC<br>PARM<br>TOTS</h3><p>PARTY SIZE<br><span class="muted">$13.99</span></p></div>
<div class="abs item" style="left:654px;top:555px"><h3>CHICKEN<br>CAESAR<br>SALAD</h3><p>PARTY SIZE<br><span class="muted">$38.99</span></p></div>
<div class="abs item" style="left:778px;top:555px"><h3>CAESAR<br>SALAD</h3><p>PARTY SIZE<br><span class="muted">$27.99</span></p></div>
<div class="abs item" style="left:898px;top:555px"><h3>ANY<br>SAUCE</h3><p>8OZ<br><span class="muted">$1.99</span></p></div>
<div class="abs item" style="left:998px;top:555px"><h3>CHEESE<br>SAUCE</h3><p>8OZ<br><span class="muted">$2.49</span></p></div>

<p class="abs learn" style="left:733px;top:657px">&#9656;LEARN MORE AT <strong>BRISKETBARN-EATS.EXAMPLE/MENU</strong></p>
</body>
</html>
```